Contemporary Media Company with Logo Needs Business Card Design

Need a modern card design for a full service digital media company using the logo included. Also want the info below on the card. Probably list the services on the card back to save space for the front. Want something contemporary to impress prospective clients. You may want to submit both a somewhat more conservative design, and then a more wild one.
General Info: (this phrase need not be on the card)
Tod Parvin
Founder and CEO
949-628-4513
tod@lumavantstudio.example
lumavantstudio.example
Services: (this word need not be on the card)
Content & Experience Strategy
Brand Development
Search Engine Optimization
Website Design
Website Operation
Social Media Integration
Complete Video Solutions
Industry/Entity Type
Business
Contact Information for Business Card
Tod Parvin
Founder and CEO
949-628-4513
tod@lumavantstudio.example
lumavantstudio.example
Brand Development
Website Design
Website Operation
Social Media Integration
Complete Video Solutions
Look and feel

```html
<!DOCTYPE html>
<html lang="en">
<head>
<meta charset="utf-8">
<title>Lumavant Studio – Business Card</title>
<link rel="stylesheet" href="https://fonts.googleapis.com/css2?family=Questrial&display=swap">
<style>
  :root {
    --page-bg: #d9d6d2;
    --card-light: #eceef0;
    --card-dark: #2e2f32;
    --accent: #d2481f;
    --text-grey: #55585c;
    --text-light: #d8d8d8;
  }
  * { margin: 0; padding: 0; box-sizing: border-box; }
  html, body {
    width: 1200px;
    height: 969px;
    overflow: hidden;
    background: var(--page-bg);
    font-family: "Questrial", "Helvetica Neue", Arial, sans-serif;
  }
  .business-card {
    position: absolute;
    left: 100px;
    top: 200px;
    width: 1000px;
    height: 570px;
    background: var(--card-light);
    box-shadow: 0 10px 30px rgba(0,0,0,0.18);
    overflow: hidden;
  }
  .card-shapes {
    position: absolute;
    inset: 0;
    width: 100%;
    height: 100%;
  }
  .services {
    position: absolute;
    left: 58px;
    top: 70px;
    list-style: none;
  }
  .services li {
    position: relative;
    padding-left: 24px;
    font-size: 22px;
    line-height: 38px;
    color: var(--text-grey);
  }
  .services li::before {
    content: "";
    position: absolute;
    left: 0;
    top: 15px;
    width: 9px;
    height: 9px;
    background: var(--accent);
  }
  .brand {
    position: absolute;
    left: 62px;
    top: 430px;
    display: flex;
    align-items: center;
    gap: 22px;
  }
  .brand-square {
    width: 70px;
    height: 70px;
    background: var(--accent);
  }
  .brand-name {
    font-size: 42px;
    letter-spacing: 3px;
    color: var(--text-grey);
    text-transform: uppercase;
  }
  .contact {
    position: absolute;
    right: 60px;
    top: 68px;
    text-align: right;
  }
  .contact-name {
    font-size: 30px;
    color: var(--accent);
    font-weight: 400;
    line-height: 40px;
  }
  .contact-title {
    font-size: 25px;
    color: var(--text-light);
    line-height: 36px;
    margin-bottom: 22px;
  }
  .contact-line {
    display: flex;
    justify-content: flex-end;
    align-items: center;
    gap: 18px;
    font-size: 21px;
    line-height: 38px;
    color: var(--text-light);
  }
  .contact-icon {
    width: 22px;
    height: 22px;
    flex: none;
  }
</style>
</head>
<body>
  <section class="business-card">
    <svg class="card-shapes" viewBox="0 0 1000 570" preserveAspectRatio="none" aria-hidden="true">
      <polygon points="434,0 1000,0 1000,570 820,570" fill="var(--card-dark)"/>
      <line x1="428" y1="-5" x2="816" y2="575" stroke="var(--accent)" stroke-width="9"/>
    </svg>

    <ul class="services">
      <li>Brand Development</li>
      <li>Website Design</li>
      <li>Website Operation</li>
      <li>Social Media Integration</li>
      <li>Complete Video Solutions</li>
      <li>Content &amp; Experience Strategy</li>
      <li>Search Engine Optimization</li>
    </ul>

    <div class="brand">
      <div class="brand-square"></div>
      <span class="brand-name">Lumavant Studio</span>
    </div>

    <div class="contact">
      <h1 class="contact-name">Tod Parvin</h1>
      <p class="contact-title">Founder and CEO</p>
      <p class="contact-line">949-628-4513
        <svg class="contact-icon" viewBox="0 0 24 24" aria-hidden="true"><path fill="var(--accent)" d="M6.6 10.8c1.4 2.8 3.8 5.1 6.6 6.6l2.2-2.2c.3-.3.7-.4 1-.2 1.1.4 2.3.6 3.6.6.6 0 1 .4 1 1V20c0 .6-.4 1-1 1C10.6 21 3 13.4 3 4c0-.6.4-1 1-1h3.5c.6 0 1 .4 1 1 0 1.3.2 2.5.6 3.6.1.3 0 .7-.2 1z"/></svg>
      </p>
      <p class="contact-line">tod@lumavantstudio.example
        <svg class="contact-icon" viewBox="0 0 24 24" aria-hidden="true"><rect x="2" y="5" width="20" height="14" fill="var(--accent)"/><polyline points="2,5 12,13 22,5" fill="none" stroke="var(--card-dark)" stroke-width="2"/></svg>
      </p>
      <p class="contact-line">lumavantstudio.example
        <svg class="contact-icon" viewBox="0 0 24 24" aria-hidden="true"><circle cx="12" cy="12" r="10" fill="var(--accent)"/><ellipse cx="12" cy="12" rx="4" ry="10" fill="none" stroke="var(--card-dark)" stroke-width="1.6"/><line x1="2" y1="12" x2="22" y2="12" stroke="var(--card-dark)" stroke-width="1.6"/></svg>
      </p>
    </div>
  </section>
</body>
</html>
```